Health IT software startup needs a product sheet to promote our software/company

-Need a one page product sheet that highlights our software and company for our customers.
-Our software is an EHR (electronic health record) software for hospitals.
-Attached is our logo (2 options-picture 4,5). Our caption with the logo should read "An EHR developed by physicians and healthcare professionals with decades of experience in behavioral health".
-Incorporate another smaller sub-heading (section) in the product sheet- titled "How Mendora Helps You"- with three associated words- 'Quality, Familiarity, Security'.
-Incorporate the main section titled "Our Software" with a description of the software with 3 components to use- see attached word document- Mendora Product Sheet.
-Attached is a optional photo you may consider if you like- we currently use it on our website with our logo and logo caption- see attached homepage-resized.jpg
-you can additional royalty free photos as needed
-Finally, the 'Contact Us' information:
404-612-8350
info@mendorasoftware.example
www.mendorasoftware.example

Target Market(s)

Behavioral Health Hospitals- specifically the product sheet will be left with the customers after we demo the software to them.

Font styles to use
Serif
Sans Serif

Colors
0555a3
3276b5
85acd3
0393ce
33a6d7
00a990
cedeed
ecf7fb
33b8a4

Requirements
Should not have
• Please do not saturate the product sheet with only colors- utilize white space

```html
<!DOCTYPE html>
<html lang="en">
<head>
<meta charset="utf-8">
<title>Mendora Product Sheet</title>
<link rel="stylesheet" href="https://fonts.googleapis.com/css2?family=Aldrich&family=Lato:wght@400;700&family=Roboto+Condensed:wght@400&family=Montserrat:wght@500&display=swap">
<style>
  :root {
    --backdrop: #a7bdd4;
    --white: #ffffff;
    --navy: #25266e;
    --navy-deep: #2b2d7c;
    --blue: #1a84d4;
    --blue-bright: #1f95e0;
    --sky: #33a6d7;
    --ink: #2d2f3a;
    --heading-dark: #1f2657;
    --body-text: #4a4c55;
    --band-dark: #3c3d40;
    --photo-light: #b7c0c9;
    --photo-dark: #7f8b97;
  }
  * { margin: 0; padding: 0; box-sizing: border-box; }
  html, body { width: 1200px; height: 2400px; overflow: hidden; }
  body { background: var(--backdrop); position: relative; font-family: "Lato", sans-serif; }

  .sheet {
    position: absolute; left: 0; top: 352px;
    width: 1200px; height: 1696px;
    background: var(--white);
    box-shadow: 0 18px 40px rgba(30, 50, 80, 0.25);
    overflow: hidden;
  }

  .brand {
    position: absolute; left: 0; top: 0; width: 100%; height: 180px;
    display: flex; align-items: center; justify-content: center; gap: 22px;
  }
  .brand-dot { width: 34px; height: 34px; border-radius: 50%; background: var(--navy); }
  .brand-name {
    font-family: "Montserrat", sans-serif; font-weight: 500;
    font-size: 66px; letter-spacing: 3px; color: var(--navy);
  }

  .tagline {
    position: absolute; left: 0; top: 180px; width: 100%; height: 116px;
    background: linear-gradient(180deg, var(--blue-bright) 0%, #1a62b8 50%, var(--navy) 100%);
    display: flex; flex-direction: column; justify-content: center; align-items: center;
    font-family: "Aldrich", sans-serif; font-size: 25px; line-height: 37px;
    color: #e8f1ff; letter-spacing: 1px; text-transform: uppercase;
  }

  .hero {
    position: absolute; left: 0; top: 302px; width: 100%; height: 516px;
    background: linear-gradient(160deg, var(--photo-light) 0%, #a1acb8 55%, var(--photo-dark) 100%);
  }

  .helps {
    position: absolute; left: 0; top: 818px; width: 100%; height: 84px;
    background: var(--band-dark); color: var(--white);
    display: flex; align-items: center;
  }
  .helps-title {
    font-family: "Roboto Condensed", sans-serif; font-size: 38px;
    margin-left: 82px; margin-right: 44px; text-transform: uppercase;
  }
  .benefit { display: flex; align-items: center; margin-right: 38px; }
  .benefit-icon {
    width: 56px; height: 56px; border-radius: 50%; background: var(--blue-bright);
    display: flex; align-items: center; justify-content: center; margin-right: 18px;
  }
  .benefit-label { font-size: 24px; }

  .product-tab {
    position: absolute; left: 345px; top: 902px; width: 520px; height: 86px;
  }
  .product-title {
    position: absolute; inset: 0; display: flex; align-items: center; justify-content: center;
    font-family: "Roboto Condensed", sans-serif; font-size: 42px; color: #dbeeff;
    text-transform: uppercase; padding-bottom: 6px;
  }

  .features { position: absolute; left: 0; top: 1020px; width: 100%; }
  .feature { position: absolute; width: 340px; text-align: center; }
  .feature.doc { left: 63px; }
  .feature.engage { left: 445px; }
  .feature.risk { left: 825px; }
  .feature-icon { height: 110px; display: flex; align-items: flex-end; justify-content: center; }
  .feature-title {
    font-family: "Roboto Condensed", sans-serif; font-size: 32px; line-height: 36px;
    margin-top: 32px; text-transform: uppercase;
  }
  .feature-title .line-dark { color: var(--heading-dark); display: block; }
  .feature-title .line-blue { color: var(--blue); display: block; }
  .feature-body {
    margin-top: 22px; font-size: 18px; line-height: 21.8px; color: var(--body-text);
    text-align: justify; text-align-last: center; hyphens: auto;
  }
  .feature-body p + p { margin-top: 22px; }

  .footer { position: absolute; left: 0; top: 1592px; width: 100%; height: 104px; }
  .call {
    position: absolute; left: 48px; top: 0; height: 100%;
    display: flex; align-items: center;
    font-family: "Lato", sans-serif; font-size: 38px; color: var(--white);
  }
  .contact {
    position: absolute; right: 56px; top: 0; height: 100%;
    display: flex; align-items: center; gap: 10px; font-size: 19px; color: var(--white);
  }
  .contact svg { margin-right: 4px; }
  .contact .gap { width: 12px; }
</style>
</head>
<body>
<main class="sheet">

  <header class="brand">
    <span class="brand-dot"></span>
    <span class="brand-name">Mendora</span>
  </header>

  <div class="tagline">
    <span>An EHR developed by physicians and healthcare professionals</span>
    <span>with decades of experience in behavioral health</span>
  </div>

  <div class="hero" role="img" aria-label="Overhead photo of a team of healthcare professionals standing in a circle on grey stone tiles, stacking their hands together"></div>

  <section class="helps">
    <h2 class="helps-title">How Mendora helps you</h2>
    <div class="benefit">
      <span class="benefit-icon">
        <svg width="30" height="30" viewBox="0 0 30 30" fill="none" stroke="#fff" stroke-width="1.8">
          <circle cx="15" cy="11" r="7"/><circle cx="15" cy="11" r="3.5"/>
          <path d="M10 17 L7 27 L11 25 L13 28 L15 18 M20 17 L23 27 L19 25 L17 28 L15 18"/>
        </svg>
      </span>
      <span class="benefit-label">Quality</span>
    </div>
    <div class="benefit">
      <span class="benefit-icon">
        <svg width="30" height="30" viewBox="0 0 30 30" fill="none" stroke="#fff" stroke-width="1.8">
          <rect x="4" y="5" width="22" height="16" rx="1.5"/>
          <path d="M8 10h8M8 14h12M8 17h6M11 25h8M15 21v4"/>
        </svg>
      </span>
      <span class="benefit-label">Familiarity</span>
    </div>
    <div class="benefit">
      <span class="benefit-icon">
        <svg width="30" height="30" viewBox="0 0 30 30" fill="none" stroke="#fff" stroke-width="1.8">
          <rect x="6" y="13" width="18" height="14" rx="1.5"/>
          <path d="M10 13V9a5 5 0 0 1 10 0v4M11 20l3 3 5-6"/>
        </svg>
      </span>
      <span class="benefit-label">Security</span>
    </div>
  </section>

  <div class="product-tab">
    <svg width="520" height="86" viewBox="0 0 520 86" aria-hidden="true">
      <defs>
        <linearGradient id="tabFill" x1="0" y1="0" x2="0" y2="1">
          <stop offset="0" stop-color="#1c7fd0"/>
          <stop offset="1" stop-color="#1f95e0"/>
        </linearGradient>
      </defs>
      <polygon points="0,0 520,0 480,86 40,86" fill="url(#tabFill)"/>
    </svg>
    <h2 class="product-title">Our Product:</h2>
  </div>

  <section class="features">
    <article class="feature doc">
      <div class="feature-icon">
        <svg width="80" height="100" viewBox="0 0 80 100" fill="none" stroke="#1f8ad8" stroke-width="4">
          <rect x="4" y="4" width="46" height="62"/>
          <rect x="14" y="14" width="46" height="62" fill="#fff"/>
          <path d="M24 24 H58 L74 40 V94 H24 Z" fill="#fff"/>
          <path d="M58 24 V40 H74"/>
        </svg>
      </div>
      <h3 class="feature-title"><span class="line-dark">Organic</span><span class="line-blue">Documentation</span></h3>
      <div class="feature-body">
        <p>Mendora set out to provide behavioral health clinicians a familiar platform to engage in chart level documentation for their patient care. Our software is built using each company's individualized workflow to provide efficient and valid information.</p>
        <p>By engaging in that recognized foundation, Mendora achieves the feel of an actual chart with the functionality of an electronic record.</p>
      </div>
    </article>

    <article class="feature engage">
      <div class="feature-icon">
        <svg width="90" height="104" viewBox="0 0 90 104" fill="#1f8ad8">
          <circle cx="48" cy="10" r="7"/>
          <path d="M44 20 h8 v20 h14 l6 18 -6 2 -5 -13 H44 Z"/>
          <path d="M36 32 a18 18 0 1 0 26 22" fill="none" stroke="#1f8ad8" stroke-width="5"/>
          <path d="M4 62 l16 6 20 22 -6 10 -30 -16 Z"/>
          <path d="M86 62 l-16 6 -20 22 6 10 30 -16 Z"/>
        </svg>
      </div>
      <h3 class="feature-title"><span class="line-dark">Patient</span><span class="line-blue">Engagement</span></h3>
      <div class="feature-body">
        <p>Using our proprietary Mendora Modules, we seamlessly digitalize therapy for use in both individual and group therapy. An optional function of the software, Mendora Modules allow the clinician to individualize therapy in a hospital setting. Furthermore, we incorporate a Family Portal through the software so that therapy can involve the entire family during the client's hospitalization.</p>
        <p>This allows the client's support system to become an integral part of the client's improvement in the hospital.</p>
      </div>
    </article>

    <article class="feature risk">
      <div class="feature-icon">
        <svg width="100" height="104" viewBox="0 0 100 104" fill="none" stroke="#1f8ad8" stroke-width="4">
          <path d="M6 50 A44 44 0 0 1 94 50 Q83 42 72 50 Q61 42 50 50 Q39 42 28 50 Q17 42 6 50 Z"/>
          <path d="M50 6 V50 M28 50 Q36 20 50 6 Q64 20 72 50"/>
          <circle cx="30" cy="70" r="7"/><path d="M16 98 V88 a14 10 0 0 1 28 0 V98 Z"/>
          <circle cx="70" cy="70" r="7"/><path d="M56 98 V88 a14 10 0 0 1 28 0 V98 Z"/>
        </svg>
      </div>
      <h3 class="feature-title"><span class="line-dark">Risk Management/</span><span class="line-blue">Quality Improvement</span></h3>
      <div class="feature-body">
        <p>To facilitate and navigate the ever-changing regulatory environment, Mendora built tailored risk management/quality improvement capabilities into the software. It is capable of tracking deficiencies in the documentation within the hospital, observing trends in real time to engage risk improvement measures, and providing data required for Quality Measures.</p>
        <p>Mendora feels this risk functionality will help identify potential errors and issues before they become systemic.</p>
      </div>
    </article>
  </section>

  <footer class="footer">
    <svg width="1200" height="104" viewBox="0 0 1200 104" style="position:absolute;left:0;top:0" aria-hidden="true">
      <defs>
        <linearGradient id="navyFill" x1="0" y1="0" x2="1" y2="0">
          <stop offset="0" stop-color="#2c3590"/>
          <stop offset="1" stop-color="#262a78"/>
        </linearGradient>
      </defs>
      <polygon points="0,0 568,0 484,104 0,104" fill="#1a8ad6"/>
      <polygon points="580,0 1200,0 1200,104 496,104" fill="url(#navyFill)"/>
      <polygon points="568,0 580,0 496,104 484,104" fill="#ffffff"/>
      <rect x="580" y="0" width="620" height="4" fill="#1a8ad6"/>
    </svg>
    <div class="call">CALL NOW 404-612-8350</div>
    <div class="contact">
      <svg width="16" height="12" viewBox="0 0 16 12" fill="none" stroke="#7fb4ee" stroke-width="1.4"><rect x="1" y="1" width="14" height="10"/><path d="M1 1l7 6 7-6"/></svg>
      <span>info@mendorasoftware.example</span>
      <span class="gap"></span>
      <svg width="14" height="14" viewBox="0 0 14 14" fill="none" stroke="#7fb4ee" stroke-width="1.2"><circle cx="7" cy="7" r="6"/><path d="M1 7h12M7 1c-3 3-3 9 0 12M7 1c3 3 3 9 0 12"/></svg>
      <span>www.mendorasoftware.example</span>
    </div>
  </footer>

</main>
</body>
</html>
```